Website for new slot-booking/reservations website/software

For a new software product we need a brand new logo and website for a reservations/booking system. The website should ideally present the main features with information text, contact info, news page as well as registration and pricing pages. As currently primary field of operation the software should be used for tennis but later on, also for other sport types. Also we'd like to be the logo a text-brand which includes the name "feldreserve.com" or just "feldreserve". The logo should ideally include an icon-design in some way. Generally we are open for ideas.

Bootstrap 4 template is a minimum requirement. (Multi-Page preferred, Single-Page still OK.)

You can use the attached image as an inspiration, but change of colors or other design elements are up to you. Currently the application has a primary color of #5500ff. The website created by you will not include the application itself, so it can have different (but ideally similar) Look&Feel.

Target Market(s)

Sports, Club-Management

Logo Text

feldreserve.com

Coding

Coded - Design and coding required

Number of Pages Required

5+ page

Font styles to use
Sans Serif

Requirements
Must have
• Bootstrap 4 Template, SCSS
Nice to have
• Rapid Loading Times, not too much external JS Libraries.
Should not have
• Extensive animations

```html
<!DOCTYPE html>
<html lang="en">
<head>
<meta charset="utf-8">
<title>feldreserve.com – Reservations made simple</title>
<link href="https://fonts.googleapis.com/css2?family=Poppins:wght@400;500;600;700&family=Nunito:wght@400;600&display=swap" rel="stylesheet">
<style>
:root{
  --brand:#4d00f5;
  --brand-deep:#4400ef;
  --lavender:#e7ddff;
  --green:#2fae6d;
  --ink:#111111;
  --text:#3a3a3a;
  --nav:#555555;
  --white:#ffffff;
  --footer:#050505;
}
*{margin:0;padding:0;box-sizing:border-box}
html,body{width:1200px;height:2855px;overflow:hidden}
body{position:relative;background:var(--white);font-family:'Nunito',sans-serif;color:var(--text)}
.abs{position:absolute}

.top-stripe{left:0;top:0;width:1200px;height:5px;background:linear-gradient(90deg,var(--green) 50%,var(--brand) 50%)}

/* header */
.brand-mark{left:196px;top:14px;width:54px;height:54px;border-radius:50%;background:var(--brand)}
.brand-name{left:110px;top:76px;width:212px;text-align:center;font:700 18px/26px 'Poppins',sans-serif;color:var(--ink)}
.main-nav{left:491px;top:38px;display:flex;gap:24px;font:600 14px/22px 'Poppins',sans-serif;color:var(--nav)}
.main-nav .active{color:var(--brand);border-bottom:2px solid var(--brand);padding-bottom:10px}
.btn{display:flex;align-items:center;justify-content:center;border-radius:30px;font-family:'Poppins',sans-serif;font-weight:700;color:var(--white);background:var(--brand);box-shadow:0 8px 14px rgba(77,0,245,.28)}
.btn-login{left:953px;top:27px;width:146px;height:47px;font-size:16px}

/* hero */
.hero-shape{left:0;top:111px}
.hero-title{left:115px;top:202px;width:560px;font:700 44px/56px 'Poppins',sans-serif;color:var(--ink)}
.hero-text{left:115px;top:325px;width:500px;font:500 15px/30px 'Poppins',sans-serif;color:var(--ink)}
.btn-register{left:115px;top:402px;width:197px;height:47px;font-size:16px}
.hero-screen{left:626px;top:283px;width:482px;height:288px;border-radius:12px;background:linear-gradient(180deg,#f4f4f7,#e3e3ea);box-shadow:0 10px 24px rgba(0,0,0,.12)}
.slider-arrows{left:1124px;top:606px;display:flex;gap:14px}

/* section heads */
.section-title{left:0;width:1200px;text-align:center;font:700 35px/44px 'Poppins',sans-serif;color:var(--ink)}
.section-title .accent{color:var(--brand)}
.section-rule{left:558px;width:84px;height:3px;background:var(--green)}

/* about */
.about-text{left:160px;top:847px;width:880px;text-align:center;font:400 15px/30px 'Nunito',sans-serif;color:var(--text)}
.btn-about{left:501px;top:1149px;width:198px;height:47px;font-size:16px}

/* pricing */
.pricing{left:0;top:1320px;width:1200px;height:614px;background:var(--brand-deep)}
.pricing-title{left:0;top:1402px;width:1200px;text-align:center;font:700 35px/44px 'Poppins',sans-serif;color:var(--white)}
.pricing-sub{left:0;top:1450px;width:1200px;text-align:center;font:400 12px/18px 'Poppins',sans-serif;color:var(--white)}
.plan{width:276px;height:276px;border-radius:50%;background:var(--white);box-shadow:0 10px 30px rgba(0,0,0,.25);text-align:center}
.plan-name{position:absolute;left:0;top:33px;width:100%;font:500 16px/22px 'Poppins',sans-serif;color:var(--ink)}
.plan-price{position:absolute;left:0;top:52px;width:100%;font:500 42px/46px 'Poppins',sans-serif;color:var(--brand)}
.plan-price small{font-size:26px;vertical-align:14px}
.plan-desc{position:absolute;left:48px;top:107px;width:180px;font:400 15px/26px 'Nunito',sans-serif;color:#6a6a6a}
.plan-btn{position:absolute;left:74px;top:199px;width:128px;height:41px;border-radius:21px;border:1.5px solid var(--brand);font:500 15px/38px 'Poppins',sans-serif;color:var(--brand)}
.plan-btn.filled{background:var(--brand);color:var(--white)}

/* news */
.news-feature{left:111px;top:2113px;width:478px;height:311px;background:linear-gradient(135deg,#d9d9db,#b5b5b9)}
.news-feature-title{left:119px;top:2440px;width:420px;font:600 23px/30px 'Poppins',sans-serif;color:var(--ink)}
.news-feature-text{left:117px;top:2515px;width:440px;font:400 15px/30px 'Nunito',sans-serif;color:var(--text)}
.btn-news{left:119px;top:2593px;width:197px;height:46px;font-size:16px}
.news-thumb{left:602px;width:180px;height:171px}
.news-item-title{left:801px;width:300px;font:600 16.5px/30px 'Poppins',sans-serif;color:var(--ink);text-transform:uppercase}
.news-item-text{left:801px;width:300px;font:400 15px/30px 'Nunito',sans-serif;color:var(--text)}

/* footer */
.site-footer{left:0;top:2747px;width:1200px;height:108px;background:var(--footer)}
.copyright{left:0;top:2788px;width:1200px;text-align:center;font:500 16px/24px 'Poppins',sans-serif;color:var(--white)}
</style>
</head>
<body>
<div class="abs top-stripe"></div>

<header>
  <div class="abs brand-mark"></div>
  <div class="abs brand-name">FELDRESERVE.COM</div>
  <nav class="abs main-nav">
    <span class="active">HOME</span><span>ABOUT US</span><span>PRICING</span><span>NEWS</span><span>CONTACT US</span>
  </nav>
  <div class="abs btn btn-login">LOGIN</div>
</header>

<section class="hero">
  <svg class="abs hero-shape" width="1200" height="570" viewBox="0 0 1200 570">
    <path d="M0 0H1200V45C1120 190 1020 390 760 490C560 570 300 590 170 470C60 370 10 260 0 170Z" fill="var(--lavender)"/>
  </svg>
  <h1 class="abs hero-title">LOREM IPSUM DOLOR SIT AMET CONSECTETUR</h1>
  <p class="abs hero-text">Lorem ipsum dolor sit amet, consectetur adipiscing elit, sed do eiusmod tempor incididunt ut labore et dolore magna aliqua.</p>
  <div class="abs btn btn-register">REGISTRATION</div>
  <div class="abs hero-screen" role="img" aria-label="Laptop showing the booking dashboard with charts and a calendar"></div>
  <svg class="abs slider-arrows" width="50" height="14" viewBox="0 0 50 14">
    <path d="M2 7H18M2 7L7 3M2 7L7 11" stroke="#111" stroke-width="2" fill="none"/>
    <path d="M32 7H48M48 7L43 3M48 7L43 11" stroke="#111" stroke-width="2" fill="none"/>
  </svg>
</section>

<section class="about">
  <h2 class="abs section-title" style="top:760px"><span class="accent">ABOUT</span> FELDRESERVE</h2>
  <div class="abs section-rule" style="top:819px"></div>
  <p class="abs about-text">Lorem ipsum dolor sit amet, consectetur adipiscing elit, sed do eiusmod tempor incididunt ut labore et dolore magna aliqua. Ut enim ad minim veniam, quis nostrud exercitation ullamco laboris nisi ut aliquip ex ea commodo consequat. Duis aute irure dolor in reprehenderit in voluptate velit esse cillum dolore eu fugiat nulla pariatur. Excepteur sint occaecat cupidatat non proident, sunt in culpa qui officia deserunt mollit anim id est laborum sit amet, consectetur adipiscing elit, sed do eiusmod tempor incididunt ut labore et dolore magna aliqua. Ut enim ad minim veniam, quis nostrud exercitation ullamco laboris nisi ut aliquip ex ea commodo consequat. Duis aute irure dolor in reprehenderit in voluptate velit esse cillum dolore eu fugiat nulla pariatur. Excepteur sint occaecat cupidatat non proident, sunt in culpa qui officia deserunt mollit anim id est laborumexercitation ullamco laboris nisi ut aliquip ex ea commodo consequat. Duis aute irure dolor in reprehenderit in voluptate velit esse cillum dolore eu fugiat nulla pariatur. Excepteur sint occaecat cupidatat non proident, sunt in culpa qui officia deserunt mollit anim id est laborum.</p>
  <div class="abs btn btn-about">LEARN MORE</div>
</section>

<section>
  <div class="abs pricing"></div>
  <h2 class="abs pricing-title">OUR PRICING PLAN</h2>
  <p class="abs pricing-sub">Lorem ipsum dolor sit amet, consectetur adipiscing elit, sed do eiusmod tempor</p>

  <div class="abs plan" style="left:145px;top:1563px">
    <div class="plan-name">Standard</div>
    <div class="plan-price">5.7 <small>$/Mon</small></div>
    <p class="plan-desc">Sed ut perspiciatis unde omnis iste natus error voluptatem</p>
    <div class="plan-btn">Learn More</div>
  </div>
  <div class="abs plan" style="left:462px;top:1520px">
    <div class="plan-name">Commercial</div>
    <div class="plan-price">3.9 <small>$/Mon</small></div>
    <p class="plan-desc">Sed ut perspiciatis unde omnis iste natus error voluptatem</p>
    <div class="plan-btn filled">Learn More</div>
  </div>
  <div class="abs plan" style="left:780px;top:1563px">
    <div class="plan-name">Personal</div>
    <div class="plan-price">6.8 <small>$/Mon</small></div>
    <p class="plan-desc">Sed ut perspiciatis unde omnis iste natus error voluptatem</p>
    <div class="plan-btn">Learn More</div>
  </div>
</section>

<section class="news">
  <h2 class="abs section-title" style="top:2018px"><span class="accent">OUR</span> LATEST NEWS</h2>
  <div class="abs section-rule" style="top:2076px"></div>

  <div class="abs news-feature" role="img" aria-label="Hands holding a tablet showing the feldreserve.com name"></div>
  <h3 class="abs news-feature-title">Lorem ipsum dolor sit amet, cons ectetur adipiscing elit.</h3>
  <p class="abs news-feature-text">Lorem ipsum dolor sit amet, consectetur adipiscing elit, sed do eiusmod tempor incididunt ut labore et magna aliqua.</p>
  <div class="abs btn btn-news">LEARN MORE</div>

  <div class="abs news-thumb" style="top:2113px;background:linear-gradient(135deg,#1d2a3a,#1e6fb0)" role="img" aria-label="Laptop screen showing a sign-in page"></div>
  <h3 class="abs news-item-title" style="top:2117px">Lorem ipsum dolor sit amet, consectetur adipisc.</h3>
  <p class="abs news-item-text" style="top:2182px">Lorem ipsum dolor sit amet, consectetur aipiscing elit, sed do eiusmod tempor incid idunt ut labore et magna aliqua.</p>

  <div class="abs news-thumb" style="top:2298px;background:linear-gradient(135deg,#c9ccd2,#6d7480)" role="img" aria-label="Person working on a laptop in an office"></div>
  <h3 class="abs news-item-title" style="top:2302px">Lorem ipsum dolor sit amet, consectetur adipisc.</h3>
  <p class="abs news-item-text" style="top:2367px">Lorem ipsum dolor sit amet, consectetur aipiscing elit, sed do eiusmod tempor incid idunt ut labore et magna aliqua.</p>

  <div class="abs news-thumb" style="top:2483px;background:linear-gradient(135deg,#b8a595,#6e6f73)" role="img" aria-label="Hand typing on a laptop keyboard"></div>
  <h3 class="abs news-item-title" style="top:2487px">Lorem ipsum dolor sit amet, consectetur adipisc.</h3>
  <p class="abs news-item-text" style="top:2552px">Lorem ipsum dolor sit amet, consectetur aipiscing elit, sed do eiusmod tempor incid idunt ut labore et magna aliqua.</p>
</section>

<footer>
  <div class="abs site-footer"></div>
  <p class="abs copyright">© Copyrights 2021 Company Name &nbsp;&nbsp;|&nbsp;&nbsp;&nbsp; All Rights Reserved</p>
</footer>
</body>
</html>
```